New Optometry Practice needs a Business Card

Need a business card for an Optometry practice called 'Marlow Family Eyecare'. I would like to use designs that are friendly, fun and professional. Looking to incorporate glasses (see uploaded image). Not interested in design with an 'eye' in logo. Like green, blue, white as color choices..but open to your ideas. Back of card will be an appointment card as well as provide address, phone and email information.

Industry/Entity Type

Business

Contact Information for Business Card

Marlow Family Eyecare
Dr. Celeste Varga, Optometrist (or O.D.)
4170 S Brackenridge Rd Wenatchee, WA 98802
CMarlowfamilyeyecare.example

Colors
acd036
33b8a4
f68d4e
cfeae6
fee18a
cadf82

Requirements
Must have
• Appointment card on back with date/time of return for next exam

```html
<!DOCTYPE html>
<html lang="en">
<head>
<meta charset="utf-8">
<title>Marlow Family Eyecare – Business Card</title>
<link href="https://fonts.googleapis.com/css2?family=Questrial&family=Montserrat:wght@400&display=swap" rel="stylesheet">
<style>
  :root {
    --teal: #00ab8f;
    --white: #ffffff;
    --orange: #e8781e;
    --backdrop: #3b3b3b;
  }
  html, body {
    margin: 0;
    padding: 0;
    overflow: hidden;
  }
  .canvas {
    width: 1200px;
    height: 1200px;
    background: var(--backdrop);
    position: relative;
    overflow: hidden;
  }
  .card {
    position: absolute;
    left: 210px;
    width: 780px;
    height: 458px;
    background: var(--white);
    overflow: hidden;
    box-shadow: 0 6px 18px rgba(0,0,0,0.35);
  }
  .card-front { top: 70px; }
  .card-back  { top: 660px; }

  .front-band {
    height: 292px;
    background: var(--teal);
    display: flex;
    flex-direction: column;
    align-items: center;
    padding-top: 70px;
    box-sizing: border-box;
  }
  .practice-name {
    font-family: "Questrial", sans-serif;
    color: var(--white);
    font-size: 46px;
    margin: 0;
    font-weight: 400;
  }
  .glasses-art {
    margin-top: 26px;
    width: 236px;
    height: 92px;
    border-radius: 46px 46px 60px 60px;
    background: var(--orange);
  }
  .front-footer {
    height: 166px;
    display: flex;
    align-items: center;
    justify-content: center;
    gap: 12px;
    font-family: "Questrial", sans-serif;
    color: var(--teal);
  }
  .doctor-name { font-size: 31px; }
  .doctor-title { font-size: 20px; }

  .back-band {
    height: 306px;
    background: var(--teal);
    display: flex;
    flex-direction: column;
    align-items: center;
    justify-content: center;
    font-family: "Montserrat", sans-serif;
    color: var(--white);
    font-size: 21px;
    line-height: 28px;
    letter-spacing: 0.5px;
    padding-bottom: 26px;
    box-sizing: border-box;
  }
  .appointment {
    height: 152px;
    display: flex;
    justify-content: space-between;
    align-items: center;
    padding: 0 58px 0 60px;
    font-family: "Montserrat", sans-serif;
    color: var(--teal);
    font-size: 19px;
    letter-spacing: 0.5px;
  }
  .appointment-field {
    display: flex;
    align-items: baseline;
    gap: 8px;
  }
  .fill-line {
    display: inline-block;
    width: 172px;
    border-bottom: 2px dotted var(--teal);
  }
</style>
</head>
<body>
<div class="canvas">

  <section class="card card-front">
    <div class="front-band">
      <h1 class="practice-name">Marlow Family Eyecare</h1>
      <div class="glasses-art" role="img" aria-label="Orange cat-eye glasses illustration"></div>
    </div>
    <div class="front-footer">
      <span class="doctor-name">Dr. Celeste Varga</span>
      <span class="doctor-title">optometrist (or O.D.)</span>
    </div>
  </section>

  <section class="card card-back">
    <div class="back-band">
      <span class="address">4170 S Brackenridge Rd Wenatchee, WA 98802</span>
      <span class="website">CMarlowfamilyeyecare.example</span>
    </div>
    <div class="appointment">
      <div class="appointment-field">Date: <span class="fill-line"></span></div>
      <div class="appointment-field">Time: <span class="fill-line"></span></div>
    </div>
  </section>

</div>
</body>
</html>
```